IT Company Business Card design

Brisk Node is a new computer solutions business focusing on setting up servers and computer systems for small to medium sized businesses.

A business client will either request a solution, or support for a current system and we will turn up on site to provide these services.

We are bast in Christchurch, New Zealand.

We are looking for unique business card's that stand out and show off the business in a professional light.

Open to all idea's etc.

Industry/Entity Type

Computer

Requirements
Must have
• Business Logo (AI file attached)
Employee Name
Business title
Business landline number
Cell phone number
Email
Web URL
Nice to have
• Could be nice to have some keywords (possibly on the back) such as:

Business IT solutions
Network installations
Phone solutions
Server management
Software diagnostics

The above is not needed, just an idea.

```html
<!DOCTYPE html>
<html lang="en">
<head>
<meta charset="utf-8">
<title>Brisk Node – Business Card</title>
<link href="https://fonts.googleapis.com/css2?family=Jost:wght@300;400&display=swap" rel="stylesheet">
<style>
  :root {
    --backdrop: #9c9c9c;
    --card: #ffffff;
    --ink: #1b1b1b;
    --muted: #6a6a6a;
    --brand-blue: #1f7fc9;
    --wash-light: #d6eaf8;
    --wash-mid: #7fb7e6;
    --wash-deep: #3a6cc4;
    --band: #3d6fc8;
    --band-text: #ffffff;
  }
  html, body {
    margin: 0;
    padding: 0;
    width: 1200px;
    height: 900px;
    overflow: hidden;
    background: var(--backdrop);
    font-family: "Jost", "Futura", sans-serif;
  }
  .card {
    position: absolute;
    left: 50px;
    top: 117px;
    width: 1100px;
    height: 666px;
    background: var(--card);
    overflow: hidden;
  }
  .card__wash {
    position: absolute;
    left: 0;
    right: 0;
    top: 330px;
    bottom: 0;
    background: linear-gradient(to bottom,
      rgba(255, 255, 255, 0) 0%,
      var(--wash-light) 30%,
      var(--wash-mid) 65%,
      var(--wash-deep) 100%);
  }
  .card__band {
    position: absolute;
    left: 0;
    right: 0;
    bottom: 0;
    height: 60px;
    background: var(--band);
  }
  .brand {
    position: absolute;
    left: 251px;
    top: 35px;
    display: flex;
    align-items: center;
    gap: 58px;
  }
  .brand__dot {
    width: 183px;
    height: 183px;
    border-radius: 50%;
    background: var(--brand-blue);
  }
  .brand__name {
    font-weight: 300;
    font-size: 66px;
    letter-spacing: 6px;
    color: var(--ink);
    text-transform: uppercase;
    line-height: 1;
  }
  .person {
    position: absolute;
    left: 502px;
    top: 213px;
  }
  .person__name {
    font-weight: 400;
    font-size: 38px;
    color: var(--ink);
    line-height: 1.1;
  }
  .person__title {
    font-weight: 400;
    font-size: 36px;
    font-variant: small-caps;
    letter-spacing: 2px;
    color: var(--muted);
    line-height: 1.1;
  }
  .contact {
    position: absolute;
    right: 39px;
    top: 316px;
    text-align: right;
    font-weight: 300;
    font-size: 32px;
    line-height: 46px;
    color: var(--ink);
  }
  .contact__line { display: block; }
  .web {
    position: absolute;
    left: 0;
    right: 0;
    bottom: 0;
    height: 60px;
    line-height: 60px;
    text-align: center;
    font-weight: 400;
    font-size: 32px;
    letter-spacing: 2px;
    color: var(--band-text);
  }
</style>
</head>
<body>
  <div class="card">
    <div class="card__wash" role="img" aria-label="Decorative flowing blue wave lines across the lower card"></div>
    <div class="card__band"></div>

    <div class="brand">
      <div class="brand__dot"></div>
      <div class="brand__name">Brisk Node</div>
    </div>

    <div class="person">
      <div class="person__name">Employee Name</div>
      <div class="person__title">Manager</div>
    </div>

    <div class="contact">
      <span class="contact__line">(03) 555 0182</span>
      <span class="contact__line">021 555 193</span>
      <span class="contact__line">employee@brisknode.co.nz</span>
    </div>

    <div class="web">WWW.BRISKNODE.CO.NZ</div>
  </div>
</body>
</html>
```